Lanterns Over The Quiet Meadow Waters Book Cover

Book cover for a new book titled "Lanterns Over The Quiet Meadow Waters" which will show how retirees can pay NO tax in their retirement. Would like you to use your creative inspiration to come up with a design.

Please make MEADOW WATERS the emphasis of the title.

can you show money being rescued, or freed, from taxes.

I'm trying convey the message that retirees can FREE themselves from the burden of taxes in retirement by reading this book and following the instructions. Think about a person swimming with a weight on his back, sinking him. Suddenly the weight is removed. The feeling and imagery of the load being light now

Doing MEADOW WATERS can alleviate many of unnecessary taxes which will weight retirees down. But, unfortunately, many advisors in my industry do not educate their clients on this stuff.

Not a fan of dark backgrounds, generally speaking. Lighter is good.

Remember folks, go to brindlecart. Type in Roth IRA books. what will jump out over the stuff that's already there? Thanks!

Target Market(s)

recent, or soon to be, retirees, people in their 50s and 60s, typically couples

Industry/Entity Type

Financial

Font styles to use
Serif

Colors

Designer to choose colors to be used in the design.

Requirements
Must have
• Be optimistic, sunny, happy. How you do that? I don't know, that's why I'm hiring you. This book is designed for the lay person, (average Joe and Jane)
• Put my picture on the lower back.
• My name at bottom of the cover
Nice to have
• Be nice to have the cover POP on Brindlecart because I'm competing with so many other books and thumbnails
• Maybe a kite with a dollar bill that is breaking from a ball and chain? Just an idea.
Should not have
• No guys in suits. Happy couples sitting on the beach or sailing. That stuff is in every piece of financial planning literature.
• NOT TECHNICAL. NO PIGGY BANKS Design please

```html
<!DOCTYPE html>
<html lang="en">
<head>
<meta charset="utf-8">
<title>Lanterns Over The Quiet Meadow Waters – Book Cover</title>
<link rel="stylesheet" href="https://fonts.googleapis.com/css2?family=Bebas+Neue&family=Oswald:wght@600;700&family=Montserrat:wght@500&display=swap">
<style>
  :root {
    --backdrop: #e9e9ea;
    --cover-top: #ffffff;
    --cover-bottom: #ececec;
    --ink: #111111;
    --blue-light: #4a93d6;
    --blue-mid: #2a6fba;
    --blue-deep: #163f7c;
    --band-top: #2d77c0;
    --band-bottom: #184b8e;
    --paper-white: #ffffff;
    --iron-light: #bdbdbd;
    --iron-dark: #4a4a4a;
  }
  * { box-sizing: border-box; margin: 0; padding: 0; }
  html, body {
    width: 1200px;
    height: 1200px;
    overflow: hidden;
    background: var(--backdrop);
  }
  .canvas {
    position: relative;
    width: 1200px;
    height: 1200px;
  }
  .book-cover {
    position: absolute;
    left: 250px;
    top: 75px;
    width: 700px;
    height: 1050px;
    background: linear-gradient(180deg, var(--cover-top) 0%, var(--cover-top) 45%, var(--cover-bottom) 100%);
    box-shadow: 0 10px 30px rgba(0,0,0,0.18);
    overflow: hidden;
  }
  .title-lead {
    position: absolute;
    top: 58px;
    left: 0;
    width: 100%;
    text-align: center;
    font-family: "Oswald", sans-serif;
    font-weight: 700;
    font-size: 56px;
    line-height: 1;
    color: var(--ink);
    letter-spacing: -0.5px;
  }
  .title-emphasis {
    position: absolute;
    top: 128px;
    left: 0;
    width: 100%;
    text-align: center;
    font-family: "Bebas Neue", sans-serif;
    font-size: 250px;
    line-height: 1;
    background: linear-gradient(180deg, var(--blue-light) 0%, var(--blue-mid) 50%, var(--blue-deep) 100%);
    -webkit-background-clip: text;
    background-clip: text;
    color: transparent;
  }
  .title-tail {
    position: absolute;
    top: 368px;
    left: 0;
    width: 100%;
    text-align: center;
    font-family: "Bebas Neue", sans-serif;
    font-size: 160px;
    line-height: 1;
    color: var(--ink);
    letter-spacing: 2px;
  }
  .freedom-illustration {
    position: absolute;
    left: 70px;
    top: 580px;
    width: 520px;
    height: 300px;
    border-radius: 50%;
    background: radial-gradient(ellipse at 30% 45%, var(--iron-dark) 0%, #7a7a7a 25%, var(--iron-light) 50%, rgba(236,236,236,0) 72%);
  }
  .author-band {
    position: absolute;
    left: 0;
    bottom: 0;
    width: 100%;
    height: 132px;
    background: linear-gradient(180deg, var(--band-top) 0%, var(--band-bottom) 100%);
    display: flex;
    align-items: center;
    justify-content: center;
  }
  .author-name {
    font-family: "Montserrat", sans-serif;
    font-weight: 500;
    font-size: 54px;
    letter-spacing: 5px;
    color: var(--paper-white);
  }
</style>
</head>
<body>
  <main class="canvas">
    <section class="book-cover">
      <h1 class="book-title">
        <span class="title-lead">Lanterns Over The Quiet</span>
        <span class="title-emphasis">MEADOW</span>
        <span class="title-tail">WATERS</span>
      </h1>
      <div class="freedom-illustration" role="img" aria-label="Iron ball marked TAX on a chain ending in an opened, broken shackle"></div>
      <footer class="author-band">
        <p class="author-name">DALE WHITMORE</p>
      </footer>
    </section>
  </main>
</body>
</html>
```